Business Card *

A business card design
Use the logo uploaded in the brief page.
You may use placeholders in your design layouts.
I will provide the actual business card details to the winning designer.

Logo
Place for contact info (name, title, phone, email, etc)

Requirements
Must have
• Logo

```html
<!DOCTYPE html>
<html lang="en">
<head>
<meta charset="utf-8">
<title>Maplecrest Agriculture and Industry – Business Card</title>
<link rel="stylesheet" href="https://fonts.googleapis.com/css2?family=Arimo:wght@400;700&display=swap">
<style>
  :root {
    --backdrop: #262626;
    --brand-green: #3bb54a;
    --card-black: #121212;
    --text-white: #ffffff;
    --text-grey: #b9b9b9;
    --divider: #444444;
  }
  * { box-sizing: border-box; margin: 0; padding: 0; }
  html, body {
    width: 1200px; height: 900px; overflow: hidden;
    background: var(--backdrop);
    font-family: "Arimo", Arial, sans-serif;
  }
  .canvas {
    position: relative; width: 1200px; height: 900px;
  }
  .card {
    position: absolute;
    width: 560px; height: 320px;
    box-shadow: 0 12px 30px rgba(0,0,0,.55);
  }
  .card--front {
    left: 90px; top: 90px;
    background: var(--brand-green);
    display: flex; align-items: center; justify-content: center;
  }
  .card--back {
    left: 550px; top: 490px;
    background: var(--card-black);
    display: flex; align-items: center;
  }
  .brand {
    display: flex; align-items: center; gap: 14px;
  }
  .brand__dot {
    width: 34px; height: 34px; border-radius: 50%;
  }
  .brand__name {
    font-weight: 700; font-size: 26px; letter-spacing: .5px;
    text-transform: uppercase; line-height: 1.15;
  }
  .card--front .brand__dot { background: var(--text-white); }
  .card--front .brand__name { color: var(--text-white); }
  .card--back .brand { width: 290px; justify-content: center; padding-left: 14px; }
  .card--back .brand__dot { background: var(--brand-green); width: 26px; height: 26px; }
  .card--back .brand__name { color: var(--text-grey); font-size: 19px; }
  .divider {
    width: 1px; height: 200px; background: var(--divider);
  }
  .contact {
    padding-left: 26px; color: var(--text-grey); font-size: 13px; line-height: 1.5;
  }
  .contact__name {
    color: var(--text-grey); font-weight: 700; font-size: 18px;
    text-transform: uppercase; line-height: 1.1;
  }
  .contact__title {
    color: var(--brand-green); font-size: 13px; text-transform: uppercase;
    margin-bottom: 12px;
  }
  .contact__row { display: flex; align-items: center; gap: 8px; }
  .contact__row svg { width: 13px; height: 13px; flex: none; }
  .contact__accent { color: var(--brand-green); }
  .contact__address { margin-top: 12px; }
</style>
</head>
<body>
<main class="canvas">
  <section class="card card--front" aria-label="Card front">
    <div class="brand">
      <span class="brand__dot"></span>
      <span class="brand__name">Maplecrest<br>Agriculture and Industry</span>
    </div>
  </section>

  <section class="card card--back" aria-label="Card back">
    <div class="brand">
      <span class="brand__dot"></span>
      <span class="brand__name">Maplecrest<br>Agriculture and Industry</span>
    </div>
    <div class="divider"></div>
    <div class="contact">
      <p class="contact__name">Daniel Harper</p>
      <p class="contact__title">Managing Director</p>
      <p class="contact__row">
        <svg viewBox="0 0 24 24" aria-hidden="true"><path fill="#3bb54a" d="M6.6 10.8a15.1 15.1 0 0 0 6.6 6.6l2.2-2.2a1 1 0 0 1 1-.25 11.4 11.4 0 0 0 3.6.57 1 1 0 0 1 1 1V20a1 1 0 0 1-1 1A17 17 0 0 1 3 4a1 1 0 0 1 1-1h3.5a1 1 0 0 1 1 1c0 1.25.2 2.45.57 3.57a1 1 0 0 1-.25 1z"/></svg>
        055-210 987 654
      </p>
      <p class="contact__row">
        <svg viewBox="0 0 24 24" aria-hidden="true"><rect x="2" y="5" width="20" height="14" fill="#3bb54a"/><path d="M2 5l10 8 10-8" fill="none" stroke="#121212" stroke-width="2"/></svg>
        info@fieldmail.com
      </p>
      <p class="contact__row">
        <svg viewBox="0 0 24 24" aria-hidden="true"><circle cx="12" cy="12" r="10" fill="none" stroke="#3bb54a" stroke-width="2"/><path d="M2 12h20M12 2c3 3 3 17 0 20M12 2c-3 3-3 17 0 20" fill="none" stroke="#3bb54a" stroke-width="1.6"/></svg>
        <span>www.<span class="contact__accent">farmsite</span>.com</span>
      </p>
      <p class="contact__address">421, Address line goes here<br>45452, Country Name</p>
    </div>
  </section>
</main>
</body>
</html>
```